Coffee Bag Design for Tidewell Coffee

We’re excited to invite you to help us bring Tidewell Coffee to life on grocery store shelves with a design that embodies our mission of spreading goodness and creating a lasting impact. Tidewell Coffee represents warmth, positivity, and the power of small actions to create ripples of goodness. Each cup not only offers a rich, gourmet coffee experience but also gives back to the community, with $2 from each bag supporting local food banks.

To reflect this vision, we’d love for the design to feature a dark (greyish) blue as the base color to convey depth and quality, complemented by a vibrant light blue that will catch the eye and add energy. Tan or gold accents could add an elegant touch and a feeling of warmth. We are aiming for a look that feels uplifting and engaging, with simplicity and elegance, yet stands out amid other brands on the shelf.

I am attaching the dimension of the bag.

Other information that needs to be listed:
Ingredients: 100% Arabica Coffee
Net Wt. 12 oz. (340 g)
Roasted and distributed by:
Name
Address
email

Text on the back of the bag:
Tidewell Coffee is crafted with a belief that kindness and positivity can spread, touching countless lives with every sip. This gourmet blend delivers a rich taste experience while giving back, as $2 from each bag sold is donated to local food banks to help those in need. Enjoy the warmth and goodness in each cup, knowing you’re making a difference with every purchase.

Thank you!

```html
<!DOCTYPE html>
<html lang="en">
<head>
<meta charset="utf-8">
<title>Tidewell Coffee – Bag Front</title>
<link href="https://fonts.googleapis.com/css2?family=Bebas+Neue&family=Roboto:wght@400&display=swap" rel="stylesheet">
<style>
  :root {
    --page-bg: #f4f4f4;
    --blue-deep: #2b5a93;
    --blue-mid: #3b6aa3;
    --blue-light: #4d7db6;
    --blue-type: #3f6aa0;
    --charcoal: #3b3b3b;
    --charcoal-dark: #2e2e2e;
    --gold-pale: #f2e39c;
    --gold: #c98f36;
    --white: #ffffff;
    --label-bg: #f3f3f5;
    --label-text: #333333;
  }
  * { box-sizing: border-box; margin: 0; padding: 0; }
  html, body { width: 1200px; height: 867px; overflow: hidden; }
  body { background: var(--page-bg); position: relative; }

  .bag-front {
    position: absolute;
    left: 365px; top: 33px;
    width: 470px; height: 800px;
    overflow: hidden;
    border-radius: 4px;
    background: var(--charcoal);
  }
  .pattern-field {
    position: absolute; left: 0; top: 0;
    width: 100%; height: 545px;
    background: linear-gradient(160deg, var(--blue-mid) 0%, var(--blue-deep) 40%, var(--blue-light) 70%, var(--blue-mid) 100%);
  }
  .seal-line {
    position: absolute; left: 0; top: 170px;
    width: 100%; height: 2px;
    background: rgba(0,0,0,0.18);
  }
  .gold-band {
    position: absolute; left: 193px; top: 0;
    width: 94px; height: 287px;
    background: linear-gradient(180deg, var(--gold-pale) 0%, var(--gold-pale) 55%, var(--gold) 100%);
  }
  .brand-dot {
    position: absolute; left: 223px; top: 395px;
    width: 24px; height: 24px; border-radius: 50%;
    background: var(--gold-pale);
  }
  .brand-name {
    position: absolute; left: 0; top: 440px; width: 100%;
    text-align: center;
    font-family: "Bebas Neue", sans-serif;
    font-size: 54px; line-height: 1;
    color: var(--white);
    letter-spacing: 0.5px;
  }
  .info-band {
    position: absolute; left: 0; top: 545px;
    width: 100%; height: 255px;
    background: linear-gradient(180deg, var(--charcoal) 0%, var(--charcoal-dark) 100%);
  }
  .purity {
    position: absolute; left: 60px; top: 126px;
    transform: rotate(-90deg);
    transform-origin: left top;
    font-family: "Bebas Neue", sans-serif;
    font-size: 66px; line-height: 1;
    color: var(--white);
  }
  .purity-wrap { position: absolute; left: 0; top: 0; }
  .origin {
    position: absolute; left: 135px; top: 40px;
    font-family: "Bebas Neue", sans-serif;
    font-size: 66px; line-height: 0.92;
    color: var(--blue-type);
  }
  .net-weight {
    position: absolute; left: 110px; top: 160px;
    font-family: "Bebas Neue", sans-serif;
    font-size: 17px; letter-spacing: 0.3px;
    color: var(--white);
  }
  .roaster-label {
    position: absolute; left: 305px; top: 40px;
    width: 140px; height: 145px;
    border-radius: 14px;
    background: var(--label-bg);
    padding: 38px 0 0 16px;
    font-family: "Roboto", sans-serif;
    font-size: 11px;
    color: var(--label-text);
  }
  .roaster-label p { margin-bottom: 18px; }
</style>
</head>
<body>
  <main class="bag-front">
    <div class="pattern-field" role="img" aria-label="Faint geometric star pattern over blue background"></div>
    <div class="seal-line"></div>
    <div class="gold-band"></div>
    <div class="brand-dot"></div>
    <h1 class="brand-name">Tidewell Coffee</h1>

    <section class="info-band">
      <div class="purity">100%</div>
      <p class="origin">ARABIC<br>COFFEE</p>
      <p class="net-weight">NET WT: 340 GM - (12 OZ)</p>
      <div class="roaster-label">
        <p>Name:</p>
        <p>Adress:</p>
        <p>Email:</p>
      </div>
    </section>
  </main>
</body>
</html>
```